Firm Stationery Design

I need a design for stationery, including: Stationery First Page, Stationery Second Sheet, Envelope, Mailing Label for Flat Envelopes, and Business Cards

```html
<!DOCTYPE html>
<html lang="en">
<head>
<meta charset="utf-8">
<title>Marlow Legal LLC – Stationery Set</title>
<link href="https://fonts.googleapis.com/css2?family=Montserrat:wght@700;800&family=Questrial&display=swap" rel="stylesheet">
<style>
:root{
  --orange:#fca000;
  --ink:#1b1b1b;
  --paper:#ffffff;
  --backdrop:#979694;
  --text:#222222;
}
*{margin:0;padding:0;box-sizing:border-box}
html,body{width:1137px;height:1200px;overflow:hidden;background:var(--backdrop)}
body{font-family:"Questrial",sans-serif;color:var(--text)}
.board{position:relative;width:1137px;height:1200px;overflow:hidden}
.sheet{position:absolute;background:var(--paper);overflow:hidden;box-shadow:6px 6px 10px rgba(0,0,0,.35)}
.sheet svg.bands{position:absolute;left:0;top:0;width:100%;height:100%}
.abs{position:absolute}
.wordmark{position:absolute;font-family:"Montserrat",sans-serif;font-weight:800;color:var(--ink);line-height:1;white-space:nowrap}
.wordmark .dot{display:inline-block;background:var(--orange);vertical-align:middle}
.contact{position:absolute;font-size:9px;line-height:1;white-space:nowrap;display:flex;align-items:center}
.tab{position:absolute;background:var(--orange);border-radius:0 6px 6px 0;display:flex;align-items:center;justify-content:flex-end;padding-right:3px}
.tab svg{width:8px;height:8px}

/* Folder cover */
.cover{left:37px;top:62px;width:500px;height:638px}
.cover .wordmark{left:138px;top:150px;font-size:44px;letter-spacing:1px}
.cover .wordmark .line2{display:block;margin-top:10px;font-size:22px;letter-spacing:9px}
.cover .tagline-main{position:absolute;left:116px;top:518px;font-family:"Montserrat",sans-serif;font-weight:700;font-size:30px;color:var(--paper)}
.cover .divider{position:absolute;left:274px;top:494px;width:1px;height:88px;background:var(--paper)}
.cover .tagline-sub{position:absolute;left:299px;top:508px;font-size:23px;line-height:24px;color:var(--paper)}

/* Letterhead */
.letterhead{left:592px;top:59px;width:500px;height:638px}
.letterhead .wordmark{left:28px;top:60px;font-size:20px}
.letterhead .wordmark .line2{display:block;margin-top:5px;font-size:10px;letter-spacing:5px}

/* Envelope */
.envelope-flap{position:absolute;left:109px;top:801px;width:521px;height:88px}
.envelope{left:109px;top:888px;width:521px;height:242px;box-shadow:6px 6px 10px rgba(0,0,0,.35)}
.envelope .wordmark{left:27px;top:60px;font-size:18px}
.envelope .wordmark .line2{display:block;margin-top:5px;font-size:9px;letter-spacing:4px}

/* Mailing label */
.label{left:756px;top:814px;width:146px;height:55px;border-radius:3px}
.label .wordmark{left:18px;top:18px;font-size:8px}
.label .wordmark .line2{display:block;margin-top:2px;font-size:4px;letter-spacing:2px}
.label .role{position:absolute;left:107px;top:9px;font-family:"Montserrat",sans-serif;font-weight:700;font-size:3.5px}
.label .name{position:absolute;left:100px;top:15px;font-family:"Montserrat",sans-serif;font-weight:700;font-size:5.5px}
.label .mini{position:absolute;font-size:3px;white-space:nowrap}

/* Business card front */
.card-front{left:707px;top:928px;width:200px;height:118px}
.card-front .wordmark{left:150px;top:26px;font-size:9px}
.card-front .wordmark .line2{display:block;margin-top:2px;font-size:4.5px;letter-spacing:2px}
.card-front .person{position:absolute;left:62px;top:45px;font-family:"Montserrat",sans-serif;font-weight:700;font-size:6px}
.card-front .title{position:absolute;left:62px;top:56px;font-size:5px;color:#666}
.card-front .mini{position:absolute;font-size:4.5px;white-space:nowrap}

/* Business card back */
.card-back{left:871px;top:1059px;width:200px;height:117px}
.card-back .wordmark{left:0;width:200px;text-align:center;top:48px;font-size:10px}
.card-back .wordmark .line2{display:block;margin-top:3px;font-size:5px;letter-spacing:2px}
</style>
</head>
<body>
<main class="board">

  <!-- Folder cover -->
  <section class="sheet cover">
    <svg class="bands" viewBox="0 0 500 638" aria-hidden="true">
      <polygon points="0,0 83,0 60,638 0,638" fill="var(--ink)"/>
      <polygon points="111,0 148,0 125,638 88,638" fill="var(--orange)"/>
      <polygon points="239,444 500,444 500,458 244,458" fill="var(--ink)"/>
      <polygon points="108,468 500,468 500,605 104,605" fill="var(--orange)"/>
    </svg>
    <div class="wordmark">MARLOW <span class="dot" style="width:18px;height:18px"></span><span class="line2">LEGAL LLC</span></div>
    <div class="tagline-main">Law Firm</div>
    <div class="divider"></div>
    <div class="tagline-sub">with Excellence<br>&amp; success</div>
  </section>

  <!-- Letterhead -->
  <section class="sheet letterhead">
    <svg class="bands" viewBox="0 0 500 638" aria-hidden="true">
      <polygon points="357,564 500,564 500,578 361,578" fill="var(--ink)"/>
      <polygon points="175,584 500,584 500,618 190,618" fill="var(--orange)"/>
    </svg>
    <div class="wordmark">MARLOW <span class="dot" style="width:9px;height:9px"></span><span class="line2">LEGAL LLC</span></div>
    <div class="tab" style="left:0;top:563px;width:40px;height:12px"><svg viewBox="0 0 10 10"><path d="M2 1l2 0 1 2-1 1c.5 1 1 1.5 2 2l1-1 2 1v2c-4 0-7-3-7-7z" fill="#fff"/></svg></div>
    <div class="contact" style="left:50px;top:565px">(555)014-2280</div>
    <div class="tab" style="left:0;top:581px;width:40px;height:12px"><svg viewBox="0 0 10 10"><path d="M5 1a3 3 0 0 1 3 3c0 2-3 5-3 5s-3-3-3-5a3 3 0 0 1 3-3z" fill="#fff"/></svg></div>
    <div class="contact" style="left:50px;top:583px">240 Harbor Lane West, USA</div>
    <div class="tab" style="left:0;top:598px;width:40px;height:12px"><svg viewBox="0 0 10 10"><circle cx="5" cy="5" r="4" fill="none" stroke="#fff"/><path d="M1 5h8M5 1v8" stroke="#fff" stroke-width=".8"/></svg></div>
    <div class="contact" style="left:50px;top:600px">www.marlowlegalllc.com</div>
    <svg class="abs" style="left:190px;top:566px;width:11px;height:8px" viewBox="0 0 11 8"><rect width="11" height="8" fill="var(--ink)"/><path d="M0 0l5.5 4.5L11 0" stroke="#fff" fill="none" stroke-width=".8"/></svg>
    <div class="contact" style="left:217px;top:566px">mail@marlowlegal.com</div>
  </section>

  <!-- Envelope -->
  <svg class="envelope-flap" viewBox="0 0 521 88" aria-hidden="true">
    <defs><linearGradient id="flapShade" x1="0" y1="0" x2="0" y2="1"><stop offset="0" stop-color="#ffffff"/><stop offset="1" stop-color="#ececec"/></linearGradient></defs>
    <polygon points="15,0 507,0 521,88 0,88" fill="url(#flapShade)"/>
  </svg>
  <section class="sheet envelope">
    <svg class="bands" viewBox="0 0 521 242" aria-hidden="true">
      <polygon points="150,205 307,205 303,219 150,219" fill="var(--orange)"/>
      <polygon points="316,205 521,205 521,219 312,219" fill="#2b2b2b"/>
    </svg>
    <div class="wordmark">MARLOW <span class="dot" style="width:8px;height:8px"></span><span class="line2">LEGAL LLC</span></div>
    <div class="tab" style="left:0;top:157px;width:42px;height:10px"><svg viewBox="0 0 10 10"><path d="M2 1l2 0 1 2-1 1c.5 1 1 1.5 2 2l1-1 2 1v2c-4 0-7-3-7-7z" fill="#fff"/></svg></div>
    <div class="contact" style="left:49px;top:158px">(555)014-2280</div>
    <div class="tab" style="left:0;top:173px;width:42px;height:10px"><svg viewBox="0 0 10 10"><path d="M5 1a3 3 0 0 1 3 3c0 2-3 5-3 5s-3-3-3-5a3 3 0 0 1 3-3z" fill="#fff"/></svg></div>
    <div class="contact" style="left:49px;top:174px">240 Harbor Lane West, USA</div>
    <div class="tab" style="left:0;top:188px;width:42px;height:10px"><svg viewBox="0 0 10 10"><rect x="1" y="2" width="8" height="6" fill="#fff"/></svg></div>
    <div class="contact" style="left:49px;top:189px">mail@marlowlegal.com</div>
    <div class="tab" style="left:0;top:204px;width:42px;height:10px"><svg viewBox="0 0 10 10"><circle cx="5" cy="5" r="4" fill="none" stroke="#fff"/><path d="M1 5h8M5 1v8" stroke="#fff" stroke-width=".8"/></svg></div>
    <div class="contact" style="left:49px;top:205px">www.marlowlegalllc.com</div>
  </section>

  <!-- Mailing label -->
  <section class="sheet label">
    <svg class="bands" viewBox="0 0 146 55" aria-hidden="true">
      <rect x="0" y="27" width="6" height="4" fill="var(--orange)"/>
      <polygon points="59,27 73,27 70,31 59,31" fill="var(--orange)"/>
      <polygon points="76,27 146,27 146,31 73,31" fill="var(--ink)"/>
      <rect x="123" y="36" width="23" height="5" rx="2.5" fill="var(--orange)"/>
      <rect x="123" y="45" width="23" height="5" rx="2.5" fill="var(--orange)"/>
    </svg>
    <div class="wordmark">MARLOW<span class="line2">LEGAL LLC</span></div>
    <div class="role">LAW FIRM</div>
    <div class="name">YOUR NAME</div>
    <div class="mini" style="left:100px;top:37px">(555)014-2280</div>
    <div class="mini" style="left:82px;top:46px">240 Harbor Ln West, USA</div>
  </section>

  <!-- Business card front -->
  <section class="sheet card-front">
    <svg class="bands" viewBox="0 0 200 118" aria-hidden="true">
      <polygon points="0,0 52,0 40,118 0,118" fill="var(--ink)"/>
      <polygon points="80,0 97,0 85,118 68,118" fill="var(--orange)"/>
      <rect x="62" y="53" width="70" height="1" fill="var(--orange)"/>
      <rect x="142" y="53" width="58" height="1" fill="#555"/>
      <rect x="62" y="74" width="18" height="4" rx="2" fill="var(--orange)"/>
      <rect x="62" y="83" width="18" height="4" rx="2" fill="var(--orange)"/>
      <polygon points="82,95 200,95 200,102 85,102" fill="var(--ink)"/>
    </svg>
    <div class="wordmark">MARLOW<span class="line2">LEGAL LLC</span></div>
    <div class="person">YOUR NAME</div>
    <div class="title">Owner</div>
    <div class="mini" style="left:87px;top:74px">(555)014-2280</div>
    <div class="mini" style="left:87px;top:83px">240 Harbor Lane West, USA</div>
    <div class="mini" style="left:105px;top:96px;color:#fff">mail@marlowlegal.com</div>
    <div class="mini" style="left:110px;top:104px">www.marlowlegalllc.com</div>
  </section>

  <!-- Business card back -->
  <section class="sheet card-back">
    <svg class="bands" viewBox="0 0 200 117" aria-hidden="true">
      <rect x="0" y="63" width="63" height="6" fill="var(--orange)"/>
      <polygon points="136,63 157,63 154,69 136,69" fill="var(--orange)"/>
      <polygon points="160,63 200,63 200,69 157,69" fill="#2b2b2b"/>
    </svg>
    <div class="wordmark">MARLOW<span class="line2">LEGAL LLC</span></div>
  </section>

</main>
</body>
</html>
```